Promotional business a5 Notepad design

I am looking for a custom a5 notepad design as a promotional item to give away to customers etc.
Attached will be a desk planner we had designed feel free to use as a reference.
We want the notepad to have lines running horizontal not squares like the desk planner example.

Industry/Entity Type

Hydraulic / industrial

Colors

Designer to choose colors to be used in the design.

```html
<!DOCTYPE html>
<html lang="en">
<head>
<meta charset="UTF-8">
<title>Meridian Hose &amp; Coupling – A5 Notepad</title>
<link rel="stylesheet" href="https://fonts.googleapis.com/css2?family=Poppins:wght@400;700&display=swap">
<style>
  :root {
    --brand-blue: #1530c4;
    --ink: #1a1a1a;
    --rule: #222222;
    --footer-text: #555555;
    --paper: #ffffff;
    --backdrop: #e6e6e6;
    --band-dark: #000000;
  }
  * { margin: 0; padding: 0; box-sizing: border-box; }
  html, body {
    width: 973px;
    height: 1200px;
    overflow: hidden;
    background: var(--backdrop);
  }
  .notepad {
    position: absolute;
    left: 62px;
    top: 0;
    width: 849px;
    height: 1200px;
    background: var(--paper);
    font-family: "Poppins", sans-serif;
  }
  .top-band {
    position: absolute;
    left: 0; top: 0;
    width: 100%;
    height: 18px;
    background: var(--brand-blue);
  }
  .bottom-band {
    position: absolute;
    left: 0; bottom: 0;
    width: 100%;
    height: 19px;
    background: var(--band-dark);
  }
  .brand {
    position: absolute;
    left: 186px;
    top: 60px;
    height: 96px;
    display: flex;
    align-items: center;
    gap: 18px;
  }
  .brand-dot {
    width: 96px;
    height: 96px;
    border-radius: 50%;
    background: var(--ink);
    flex: none;
  }
  .brand-name {
    font-weight: 700;
    font-size: 30px;
    line-height: 1;
    letter-spacing: 1px;
    color: var(--brand-blue);
    text-transform: uppercase;
    white-space: nowrap;
  }
  .ruled-lines {
    position: absolute;
    left: 70px;
    top: 221px;
    width: 711px;
    list-style: none;
  }
  .ruled-lines li {
    height: 2px;
    background: var(--rule);
    margin-bottom: 61px;
  }
  .ruled-lines li:last-child { margin-bottom: 0; }
  .contact {
    position: absolute;
    left: 0;
    top: 1100px;
    width: 100%;
    text-align: center;
    font-size: 14px;
    line-height: 20px;
    color: var(--footer-text);
  }
</style>
</head>
<body>
  <main class="notepad">
    <div class="top-band"></div>

    <header class="brand">
      <span class="brand-dot"></span>
      <span class="brand-name">Meridian Hose &amp; Coupling</span>
    </header>

    <ul class="ruled-lines">
      <li></li><li></li><li></li><li></li><li></li><li></li><li></li>
      <li></li><li></li><li></li><li></li><li></li><li></li><li></li>
    </ul>

    <footer class="contact">
      <p>P. 555-014-2298 E. name@meridianhose.com W. www.meridianhose.com</p>
      <p>2318 Foundry Way, Kenai, Alaska 99611</p>
    </footer>

    <div class="bottom-band"></div>
  </main>
</body>
</html>
```